Non fiction book cover. The book advises how to get a new job.

The book size will be 20cm high by 13cm wide and I need a front cover which can wrap around to the back. This book has a serious message, but I've tried to make it quite light to read and accessible. So I don't want a cover that is too dour or serious and not frivolous either. At the end of the project, I will need a high resolution 3D image of the book, included as part of the package.<br/>The Title of the book is:- "Past Your Prime? Hunting for the Next Role?<br/>by Gerald Whitcombe-Prynne".<br/>I am thinking of a light yellow background, with a striking image to attract attention. The image and words should be clear and sharp.<br/>Here is the, BACK COVER wording.<br/>"This book tells you clearly and simply the steps that you need to take, to get a job, once you’re over 50.<br/>It advises you on the techniques to use to write a killer CV.<br/>It explains how to ensure that your CV attention.<br/>It shows the best way to approach your local job agency.<br/>It demonstrates the best way to use your network.<br/><br/>This book, written by someone with 30 years’ experience in the recruitment industry, gives you ALL the answers.<br/>Whether you are a top executive or someone after some local part time work, then this book is for you. <br/>With the help of this book you will secure your next position.<br/>

Target Market(s)

UK, over 50s, male and female.

Font styles to use
Serif

Colors
fbee3e

Requirements
Must have
• A clear uncluttered cover.
Should not have
• Fussy and over complicated

```html
<!DOCTYPE html>
<html lang="en">
<head>
<meta charset="utf-8">
<title>Past Your Prime? Hunting for the Next Role? – Cover Wrap</title>
<link rel="stylesheet" href="https://fonts.googleapis.com/css2?family=Bebas+Neue&family=Oswald:wght@300;600&display=swap">
<style>
  :root {
    --cover-yellow: #fbf000;
    --ink-navy: #0e2a3c;
    --spine-text: #f4ec9a;
    --card-white: #ffffff;
    --card-warm: #e6d9d0;
    --stage: #f4f4f4;
    --art-yellow: #f7e43c;
    --art-blue: #2a5a7c;
  }
  * { margin: 0; padding: 0; box-sizing: border-box; }
  html, body { width: 899px; height: 1200px; overflow: hidden; }
  body { background: var(--stage); position: relative; }

  .cover-wrap {
    position: absolute;
    left: 11px; top: 296px;
    width: 877px; height: 608px;
    background: var(--cover-yellow);
    overflow: hidden;
  }

  /* Back cover */
  .back-cover {
    position: absolute; left: 0; top: 0;
    width: 405px; height: 608px;
    padding: 52px 6px 0;
    text-align: center;
    color: var(--ink-navy);
    font-family: "Oswald", sans-serif;
    font-weight: 300;
    font-size: 9.5px;
    line-height: 1.65;
    text-transform: uppercase;
  }
  .back-cover p { margin-bottom: 14px; }
  .back-cover .blurb-strong { font-weight: 600; font-size: 9.5px; }
  .back-cover .benefits { margin-bottom: 14px; }

  /* Spine */
  .spine {
    position: absolute; left: 405px; top: 0;
    width: 68px; height: 608px;
    background: var(--ink-navy);
  }
  .spine-title, .spine-author {
    position: absolute;
    left: 50%;
    white-space: nowrap;
    font-family: "Bebas Neue", sans-serif;
  }
  .spine-title {
    top: 222px;
    font-size: 25px;
    color: var(--spine-text);
    transform: translate(-50%, -50%) rotate(90deg);
  }
  .spine-author {
    top: 520px;
    font-size: 15px;
    color: var(--cover-yellow);
    transform: translate(-50%, -50%) rotate(90deg);
  }

  /* Front cover */
  .front-cover { position: absolute; left: 473px; top: 0; width: 404px; height: 608px; }
  .title-card {
    position: absolute; left: 36px; top: 39px;
    width: 334px; height: 462px;
    overflow: hidden;
    background: linear-gradient(225deg, var(--card-warm) 0%, var(--card-white) 40%, var(--card-white) 100%);
    box-shadow: 0 2px 6px rgba(0,0,0,0.25);
  }
  .book-title {
    position: absolute; left: 0; top: 14px; width: 100%;
    text-align: center;
    font-family: "Bebas Neue", sans-serif;
    font-weight: 400;
    color: var(--ink-navy);
    line-height: 0.95;
  }
  .book-title .line-lead { display: block; font-size: 56px; }
  .book-title .line-middle { display: block; font-size: 42px; margin-top: 6px; }
  .book-title .line-punch { display: block; font-size: 78px; margin-top: 6px; }

  .handshake-art {
    position: absolute; left: 0; top: 206px;
    width: 334px; height: 256px;
    background:
      radial-gradient(circle at 50% 62%, var(--art-yellow) 0%, rgba(247,228,60,0.85) 30%, rgba(247,228,60,0) 60%),
      linear-gradient(90deg, rgba(42,90,124,0.35) 0%, rgba(42,90,124,0) 30%, rgba(42,90,124,0) 70%, rgba(42,90,124,0.35) 100%);
  }

  .author-name {
    position: absolute; left: 0; top: 534px; width: 404px;
    text-align: center;
    font-family: "Bebas Neue", sans-serif;
    font-size: 37px;
    color: var(--ink-navy);
    white-space: nowrap;
  }
</style>
</head>
<body>
  <div class="cover-wrap">
    <section class="back-cover">
      <p class="blurb-strong">This book tells you clearly and simply the steps that you need to take, to get a job,<br>once you’re over 50.</p>
      <div class="benefits">
        -It advises you on the techniques to use to write a killer CV.<br>
        -It explains how to ensure that your CV attention.<br>
        -It shows the best way to approach your local job agency.<br>
        -It demonstrates the best way to use your network.
      </div>
      <p class="blurb-strong">This book, written by someone with 30 years’ experience in the recruitment<br>industry, gives you all the answers.</p>
      <p>Whether you are a top executive or someone after some local part time work,<br>then this book is for you.</p>
      <p>With the help of this book you will secure your next position.</p>
    </section>

    <section class="spine">
      <div class="spine-title">Past Your Prime? Hunting for the Next Role?</div>
      <div class="spine-author">Gerald Whitcombe-Prynne</div>
    </section>

    <section class="front-cover">
      <div class="title-card">
        <h1 class="book-title">
          <span class="line-lead">Past Your Prime?</span>
          <span class="line-middle">Hunting for the</span>
          <span class="line-punch">Next Role?</span>
        </h1>
        <div class="handshake-art" role="img" aria-label="Illustration: two suited arms meeting in a handshake in front of a yellow circle"></div>
      </div>
      <div class="author-name">Gerald Whitcombe-Prynne</div>
    </section>
  </div>
</body>
</html>
```